Customer Journey Graphic

I want to graphic to describe a marketing framework I am teaching a course on

It a framework for growing a business
The idea is we
get customers to "take a Journey" through 7 steps
to deliver value to them

There are 4 major concepts that impact this journey - Game Plan, Business Model, "Inside out thinking' and Unique Competitive advantage
These concepts can make the journey faster, get more people to take it or make it more valuable

The stages are

- Target
- attract
- nurture
- convert
- maximise
- loyalty
- reactivation

I want to uses this framework as an overall;; 'explainer' fro my idea ,so it must looks very professional, and work well in presentations

I have included a rought 'sketch; of my thinking as an attachment

Business Owners

Business

Serif

• clear, get acroess the idea of a Journye over times, teh idea you can improve your results throught applying concpets of ' business model', "inside out thinking: , unique competitive advantage and game plane

```html
<!DOCTYPE html>
<html lang="en">
<head>
<meta charset="utf-8">
<title>Customer Journey Framework</title>
<link rel="stylesheet" href="https://fonts.googleapis.com/css2?family=Roboto+Condensed:ital,wght@0,700;1,400&display=swap">
<style>
  :root {
    --canvas: #ffffff;
    --stage: #333333;
    --stage-edge: #ffffff;
    --label: #ffffff;
    --blue: #1b75bc;
    --orange: #f7941d;
    --red: #ef4136;
    --green: #8dc63f;
  }
  * { margin: 0; padding: 0; box-sizing: border-box; }
  html, body { width: 1200px; height: 750px; overflow: hidden; background: var(--canvas); }
  .framework { display: block; width: 1200px; height: 750px; }
  .concept-band { fill: none; stroke-width: 60; }
  .concept-teeth { fill: none; stroke-width: 20; stroke-dasharray: 26 22; }
  .concept-label {
    font-family: "Roboto Condensed", "Arial Narrow", sans-serif;
    font-weight: 700; font-size: 29px; fill: var(--label);
  }
  .concept-label.small { font-size: 25px; }
  .direction-arrow { stroke: var(--stage-edge); stroke-width: 5; stroke-linejoin: miter; }
  .stage-shape { fill: var(--stage); stroke: var(--stage-edge); stroke-width: 4; stroke-linejoin: miter; }
  .stage-icon { fill: none; stroke: var(--label); stroke-width: 3.5; stroke-linecap: round; stroke-linejoin: round; }
  .stage-icon .solid { fill: var(--label); stroke: none; }
  .stage-label {
    font-family: "Roboto Condensed", "Arial Narrow", sans-serif;
    font-style: italic; font-weight: 400; font-size: 19px; fill: var(--label);
    text-anchor: middle;
  }
  .accent-line { stroke-width: 4; }
</style>
</head>
<body>
<svg class="framework" viewBox="0 0 1200 750" xmlns="http://www.w3.org/2000/svg" role="img" aria-label="Customer journey: seven stages driven by four concepts">
  <defs>
    <linearGradient id="grad-business-model" gradientUnits="userSpaceOnUse" x1="330" y1="375" x2="600" y2="105">
      <stop offset="0.15" stop-color="var(--blue)"/><stop offset="0.75" stop-color="var(--orange)"/>
    </linearGradient>
    <linearGradient id="grad-inside-out" gradientUnits="userSpaceOnUse" x1="600" y1="105" x2="870" y2="375">
      <stop offset="0.2" stop-color="var(--orange)"/><stop offset="0.8" stop-color="var(--red)"/>
    </linearGradient>
    <linearGradient id="grad-advantage" gradientUnits="userSpaceOnUse" x1="870" y1="375" x2="600" y2="645">
      <stop offset="0.2" stop-color="var(--red)"/><stop offset="0.8" stop-color="var(--green)"/>
    </linearGradient>
    <linearGradient id="grad-game-plan" gradientUnits="userSpaceOnUse" x1="600" y1="645" x2="330" y2="375">
      <stop offset="0.2" stop-color="var(--green)"/><stop offset="0.8" stop-color="var(--blue)"/>
    </linearGradient>

    <path id="path-business-model" d="M330 375 A270 270 0 0 1 581.2 105.7"/>
    <path id="path-inside-out" d="M618.8 105.7 A270 270 0 0 1 870 375"/>
    <path id="path-advantage" d="M870 375 A270 270 0 0 1 618.8 644.4"/>
    <path id="path-game-plan" d="M581.2 644.4 A270 270 0 0 1 330 375"/>

    <path id="text-business-model" d="M340 375 A260 260 0 0 1 600 115"/>
    <path id="text-inside-out" d="M600 115 A260 260 0 0 1 860 375"/>
    <path id="text-game-plan" d="M318 375 A282 282 0 0 0 600 657"/>
    <path id="text-advantage-1" d="M600 662 A287 287 0 0 0 887 375"/>
    <path id="text-advantage-2" d="M600 638 A263 263 0 0 0 863 375"/>
  </defs>

  <!-- Concept ring -->
  <g class="concept concept-business-model">
    <use href="#path-business-model" class="concept-teeth" stroke="url(#grad-business-model)" transform="translate(600 375) scale(1.145) translate(-600 -375)"/>
    <use href="#path-business-model" class="concept-band" stroke="url(#grad-business-model)"/>
  </g>
  <g class="concept concept-inside-out">
    <use href="#path-inside-out" class="concept-teeth" stroke="url(#grad-inside-out)" transform="translate(600 375) scale(1.145) translate(-600 -375)"/>
    <use href="#path-inside-out" class="concept-band" stroke="url(#grad-inside-out)"/>
  </g>
  <g class="concept concept-advantage">
    <use href="#path-advantage" class="concept-teeth" stroke="url(#grad-advantage)" transform="translate(600 375) scale(1.145) translate(-600 -375)"/>
    <use href="#path-advantage" class="concept-band" stroke="url(#grad-advantage)"/>
  </g>
  <g class="concept concept-game-plan">
    <use href="#path-game-plan" class="concept-teeth" stroke="url(#grad-game-plan)" transform="translate(600 375) scale(1.145) translate(-600 -375)"/>
    <use href="#path-game-plan" class="concept-band" stroke="url(#grad-game-plan)"/>
  </g>

  <polygon class="direction-arrow" points="573,58 573,152 632,105" fill="var(--orange)"/>
  <polygon class="direction-arrow" points="627,598 627,692 568,645" fill="var(--green)"/>

  <text class="concept-label"><textPath href="#text-business-model" startOffset="50%" text-anchor="middle">Business Model</textPath></text>
  <text class="concept-label"><textPath href="#text-inside-out" startOffset="50%" text-anchor="middle">Inside-Out Thinking</textPath></text>
  <text class="concept-label"><textPath href="#text-game-plan" startOffset="55%" text-anchor="middle">Game Plan</textPath></text>
  <text class="concept-label small"><textPath href="#text-advantage-1" startOffset="50%" text-anchor="middle">Unique Competitive</textPath></text>
  <text class="concept-label small"><textPath href="#text-advantage-2" startOffset="50%" text-anchor="middle">Advantage</textPath></text>

  <line class="accent-line" x1="282" y1="312" x2="332" y2="312" stroke="var(--blue)"/>
  <line class="accent-line" x1="268" y1="444" x2="330" y2="444" stroke="var(--blue)"/>
  <line class="accent-line" x1="775" y1="312" x2="872" y2="312" stroke="var(--red)"/>

  <!-- Journey stages -->
  <g class="journey">
    <g class="stage stage-target">
      <polygon class="stage-shape" points="82,322 206,322 228,379 206,436 82,436 104,379"/>
      <g class="stage-icon"><circle cx="155" cy="362" r="16"/><circle cx="155" cy="362" r="8"/><circle class="solid" cx="155" cy="362" r="3"/><line x1="155" y1="362" x2="172" y2="345"/></g>
      <text class="stage-label" x="158" y="419">Target</text>
    </g>
    <g class="stage stage-attract">
      <polygon class="stage-shape" points="228,322 352,322 374,379 352,436 228,436 250,379"/>
      <g class="stage-icon"><path d="M290 350 v14 a12 12 0 0 0 24 0 v-14"/><line x1="284" y1="350" x2="296" y2="350"/><line x1="308" y1="350" x2="320" y2="350"/><line x1="296" y1="342" x2="290" y2="336"/><line x1="308" y1="342" x2="314" y2="336"/></g>
      <text class="stage-label" x="304" y="419">Attract</text>
    </g>
    <g class="stage stage-nurture">
      <polygon class="stage-shape" points="374,322 498,322 520,379 498,436 374,436 396,379"/>
      <g class="stage-icon"><path d="M450 372 v-18"/><path class="solid" d="M450 356 c-2 -12 -12 -16 -20 -14 c2 10 10 16 20 14z"/><path class="solid" d="M450 352 c2 -10 10 -14 18 -12 c-2 8 -8 13 -18 12z"/><path d="M428 370 c8 6 18 8 28 6 l14 -6"/></g>
      <text class="stage-label" x="450" y="419">Nurture</text>
    </g>
    <g class="stage stage-convert">
      <polygon class="stage-shape" points="520,322 644,322 666,379 644,436 520,436 542,379"/>
      <g class="stage-icon"><path d="M582 356 a16 16 0 0 1 28 -6"/><polyline points="612,342 611,351 602,350"/><path d="M610 366 a16 16 0 0 1 -28 6"/><polyline points="580,380 581,371 590,372"/></g>
      <text class="stage-label" x="596" y="419">Convert</text>
    </g>
    <g class="stage stage-maximise">
      <polygon class="stage-shape" points="666,322 790,322 812,379 790,436 666,436 688,379"/>
      <g class="stage-icon"><rect class="solid" x="726" y="362" width="6" height="12"/><rect class="solid" x="736" y="354" width="6" height="20"/><rect class="solid" x="746" y="346" width="6" height="28"/><rect class="solid" x="756" y="338" width="6" height="36"/><polyline points="724,352 744,338"/><polyline points="738,336 745,337 744,344"/></g>
      <text class="stage-label" x="742" y="419">Maximise</text>
    </g>
    <g class="stage stage-loyalty">
      <polygon class="stage-shape" points="812,322 936,322 958,379 936,436 812,436 834,379"/>
      <g class="stage-icon"><path d="M862 358 l10 -10 h10 l8 6 l10 -6 l10 10"/><path d="M872 362 l12 12 a3 3 0 0 0 5 -4 l-4 -4 m4 4 a3 3 0 0 0 5 -4 l-4 -4 m4 4 a3 3 0 0 0 5 -4 l-8 -8"/><path d="M882 348 l-8 8 a3 3 0 0 0 4 4 l8 -6"/></g>
      <text class="stage-label" x="888" y="419">Loyalty</text>
    </g>
    <g class="stage stage-reactivation">
      <polygon class="stage-shape" points="958,322 1082,322 1104,379 1082,436 958,436 980,379"/>
      <g class="stage-icon"><path d="M1024 346 a15 15 0 1 1 -8 26"/><polyline points="1016,340 1024,346 1017,353"/></g>
      <text class="stage-label" x="1034" y="419">Reactivation</text>
    </g>
  </g>
</svg>
</body>
</html>
```